Marrowind Estates Wine Label

We are seeking a new brand label image for our 20+ year old wine brand Marrowind. Our current label is very basic and we are seeking something ELEGANT and MODERN but also MORE EYE-CATCHING.

The label art needs to incorporate our existing fairy image (please see attached images) which can be in color or in black and white line art.

The fairy image should be a smaller component of the design—not the main aspect—and should be placed as a discreet logo somewhere on the label.

We want a more modern, elegant and exciting look. One that builds on the Brandname Marrowind downplays the ICON Faerie but enhances our brand name's equity.

Update: May 26
1. Logo PSD file attached
-Logo File/Font info: For 600dpi resolution, MARROWIND is 40pt Berhard Modern BT (in bold, standard spacing). ESTATES is 13pt with 178% spacing)

2. The size is variable, and dependent on whether we do 1 larger (longer) label that wraps around the bottle, or 2 separate labels. Our current labels are 4.5” square for front and 3.5” for back (see file attached).

additional notes: we can put the alcohol and volume size on the back label. And/or we can make a “front” label that is legally submitted as the back label (and vice versa… see attached Tamber Owlet labels).

Target Market(s)

Wine drinkers!

Font styles to use
Other font styles liked:
• Our logo text is Bernhard Modern Bold

Requirements
Nice to have
• See description

```html
<!DOCTYPE html>
<html lang="en">
<head>
<meta charset="utf-8">
<title>Marrowind Estates – Brambleigh Reserve Label</title>
<link rel="stylesheet" href="https://fonts.googleapis.com/css2?family=Cormorant+Garamond:wght@500;600;700&display=swap">
<style>
  :root {
    --bg-top: #f3f3f4;
    --bg-bottom: #a9acb2;
    --gold-light: #f4dc9c;
    --gold: #d9b066;
    --gold-deep: #a87b34;
    --teal: #0f5f78;
    --teal-dark: #083f52;
    --seal-dark: #2a2a2c;
    --ink: #1f1a12;
  }
  html, body {
    margin: 0;
    padding: 0;
    width: 1161px;
    height: 1200px;
    overflow: hidden;
  }
  body {
    background: linear-gradient(180deg, var(--bg-top) 0%, var(--bg-bottom) 100%);
    font-family: "Cormorant Garamond", Georgia, serif;
  }
  .canvas {
    position: relative;
    width: 1161px;
    height: 1200px;
  }
  .wine-label {
    position: absolute;
    left: 60px;
    top: 180px;
    width: 1040px;
    height: 848px;
  }
  .label-text { font-family: "Cormorant Garamond", Georgia, serif; }
  .wine-name { font-size: 34px; font-weight: 700; fill: var(--gold); }
  .wine-detail { font-size: 12.5px; font-weight: 500; fill: var(--gold-light); letter-spacing: 0.4px; }
  .brand-name { font-size: 30px; font-weight: 600; fill: var(--gold); letter-spacing: 1px; }
  .brand-sub { font-size: 9px; font-weight: 600; fill: var(--gold); letter-spacing: 4px; }
  .vintage { font-size: 40px; font-weight: 600; fill: var(--ink); letter-spacing: 1px; }
</style>
</head>
<body>
<main class="canvas">
  <svg class="wine-label" viewBox="0 0 760 620" xmlns="http://www.w3.org/2000/svg" aria-label="Marrowind Estates Brambleigh Reserve wine label">
    <defs>
      <linearGradient id="gold-fill" x1="0" y1="0" x2="1" y2="1">
        <stop offset="0" stop-color="var(--gold-light)"/>
        <stop offset="0.5" stop-color="var(--gold)"/>
        <stop offset="1" stop-color="var(--gold-deep)"/>
      </linearGradient>
      <linearGradient id="ribbon-fill" x1="0" y1="0" x2="0" y2="1">
        <stop offset="0" stop-color="var(--gold-light)"/>
        <stop offset="0.6" stop-color="var(--gold)"/>
        <stop offset="1" stop-color="var(--gold-deep)"/>
      </linearGradient>
      <linearGradient id="teal-fill" x1="0" y1="0" x2="1" y2="0">
        <stop offset="0" stop-color="var(--teal-dark)"/>
        <stop offset="0.5" stop-color="var(--teal)"/>
        <stop offset="1" stop-color="var(--teal-dark)"/>
      </linearGradient>
      <radialGradient id="seal-fill" cx="0.5" cy="0.35" r="0.7">
        <stop offset="0" stop-color="#4a4a4e"/>
        <stop offset="1" stop-color="var(--seal-dark)"/>
      </radialGradient>
      <path id="vintage-arc" d="M185,580 Q380,535 575,562"/>
    </defs>

    <!-- side flourishes -->
    <ellipse class="flourish" cx="55" cy="170" rx="44" ry="28" fill="url(#gold-fill)" opacity="0.75" role="img" aria-label="Gold leaf flourish ornament"/>
    <ellipse class="flourish" cx="705" cy="170" rx="44" ry="28" fill="url(#gold-fill)" opacity="0.75" role="img" aria-label="Gold leaf flourish ornament"/>

    <!-- upper tabs behind centre -->
    <rect class="upper-tab" x="160" y="110" width="440" height="100" rx="18" fill="url(#gold-fill)"/>
    <rect class="upper-tab-inner" x="168" y="118" width="424" height="92" rx="14" fill="url(#teal-fill)"/>

    <!-- left panel -->
    <path class="side-panel" d="M10,190 Q55,190 60,172 L262,172 L262,505 L60,505 Q55,470 10,470 Q34,330 10,190 Z" fill="url(#gold-fill)"/>
    <path class="side-panel-inner" d="M24,202 Q62,200 70,184 L254,184 L254,494 L70,494 Q62,462 24,460 Q44,330 24,202 Z" fill="url(#teal-fill)"/>

    <!-- right panel -->
    <path class="side-panel" d="M750,190 Q705,190 700,172 L498,172 L498,505 L700,505 Q705,470 750,470 Q726,330 750,190 Z" fill="url(#gold-fill)"/>
    <path class="side-panel-inner" d="M736,202 Q698,200 690,184 L506,184 L506,494 L690,494 Q698,462 736,460 Q716,330 736,202 Z" fill="url(#teal-fill)"/>

    <!-- centre panel -->
    <rect class="centre-panel" x="236" y="160" width="288" height="390" rx="16" fill="url(#gold-fill)"/>
    <rect class="centre-panel-inner" x="250" y="172" width="260" height="370" rx="10" fill="#0c5467" role="img" aria-label="Teal lattice pattern background"/>

    <!-- seal -->
    <circle class="seal-teeth" cx="380" cy="128" r="112" fill="none" stroke="url(#gold-fill)" stroke-width="16" stroke-dasharray="6 5"/>
    <circle class="seal-ring" cx="380" cy="128" r="106" fill="url(#gold-fill)"/>
    <circle class="seal-face" cx="380" cy="128" r="90" fill="url(#seal-fill)"/>
    <rect class="seal-emblem" x="318" y="62" width="124" height="120" rx="8" fill="var(--gold)" opacity="0.55" role="img" aria-label="Gold crown above a row of five stars"/>

    <!-- brand -->
    <text class="label-text brand-name" x="380" y="286" text-anchor="middle">MARROWIND</text>
    <text class="label-text brand-sub" x="382" y="302" text-anchor="middle">ESTATES</text>
    <line x1="318" y1="314" x2="442" y2="314" stroke="var(--gold)" stroke-width="1"/>
    <rect class="fairy-mark" x="338" y="330" width="84" height="150" rx="36" fill="#c98a4a" opacity="0.6" role="img" aria-label="Winged fairy figure illustration"/>

    <!-- side texts -->
    <text class="label-text wine-name" x="132" y="306" text-anchor="middle">Brambleigh</text>
    <text class="label-text wine-detail" x="132" y="334" text-anchor="middle">ALC. 13.01% BY VOL.</text>
    <text class="label-text wine-name" x="628" y="306" text-anchor="middle">Reserve</text>
    <text class="label-text wine-detail" x="628" y="334" text-anchor="middle">750ml</text>

    <!-- ribbon -->
    <path class="ribbon-tail" d="M64,500 L200,486 L214,560 L78,580 Q88,545 64,500 Z" fill="url(#ribbon-fill)"/>
    <path class="ribbon-tail" d="M696,500 L560,486 L546,560 L682,580 Q672,545 696,500 Z" fill="url(#ribbon-fill)"/>
    <path class="ribbon-band" d="M170,520 Q380,470 590,505 L590,585 Q380,555 170,610 Z" fill="url(#ribbon-fill)" stroke="var(--gold-deep)" stroke-width="1.5"/>
    <text class="label-text vintage" text-anchor="middle">
      <textPath href="#vintage-arc" startOffset="50%">NORTON 2015</textPath>
    </text>
  </svg>
</main>
</body>
</html>
```